Author of female self help book in need of cover that expresses freedom and empowerment

This is the first in a series of female self help books. It is called Her Quiet Compass. The book tells my story of hitting rock bottom, winning the lottery, and discovering what I call my Quiet Compass. The purpose of the book is to help inspire women to break free from the pain of loss including divorce, job loss, or heartbreak. It will help guide a women's journey to finding their courage and motivation to move on in pursuit of happiness and joy. She will gain skills to help build resilience, tap into her inner strength, achieve success in her personal and professional life and finally create a life she loves to live.

Target Market(s)

Women 30-60 yrs, divorced, single mother, widow, working professional

Industry/Entity Type

Life Coaching

Font styles to use
Serif

Colors
fbd4d5
f59296

Requirements
Must have
• Cover must express female freedom and empowerment.
Nice to have
• I would like to see something like a mountain top scene or woman depicted with arms raised high in victory.

```html
<!DOCTYPE html>
<html lang="en">
<head>
<meta charset="utf-8">
<title>Her Quiet Compass — Book Cover</title>
<link rel="stylesheet" href="https://fonts.googleapis.com/css2?family=Cinzel:wght@400;500;600&family=Oswald:wght@500&display=swap">
<style>
  :root {
    --sky-lilac: #d9b2ea;
    --sky-pink: #f2b8d8;
    --sky-blush: #fbd4d5;
    --horizon-peach: #f7c9a8;
    --sea-deep: #2f7f93;
    --sea-teal: #4fb6c9;
    --water-cyan: #38c4ea;
    --water-blue: #1c9ad3;
    --cloud-white: #ffffff;
    --title-rose: #f59296;
    --title-red: #e0324f;
    --title-plum: #4a2350;
    --author-white: #ffffff;
  }

  * { margin: 0; padding: 0; box-sizing: border-box; }

  html, body {
    width: 800px;
    height: 1200px;
    overflow: hidden;
    background: #ffffff;
  }

  .cover {
    position: relative;
    width: 800px;
    height: 1200px;
    overflow: hidden;
  }

  .cover-scene {
    position: absolute;
    inset: 0;
    background:
      radial-gradient(ellipse 420px 230px at 400px 760px, rgba(255,255,255,0.95), rgba(255,255,255,0) 75%),
      radial-gradient(ellipse 300px 80px at 420px 500px, rgba(255,255,255,0.85), rgba(255,255,255,0) 80%),
      radial-gradient(ellipse 240px 160px at 380px 190px, rgba(255,240,250,0.85), rgba(255,255,255,0) 80%),
      linear-gradient(180deg,
        var(--sky-lilac) 0px,
        var(--sky-pink) 150px,
        #f3d2ea 250px,
        var(--sky-blush) 330px,
        var(--horizon-peach) 395px,
        var(--sea-deep) 412px,
        var(--sea-teal) 450px,
        var(--water-cyan) 540px,
        #bfeefb 700px,
        #d9f5fd 820px,
        var(--water-cyan) 1000px,
        var(--water-blue) 1200px);
  }

  .cover-title {
    position: absolute;
    left: 0;
    top: 690px;
    width: 800px;
    font-family: "Cinzel", serif;
    font-weight: 500;
    line-height: 1;
    background: linear-gradient(100deg, var(--title-plum) 0%, var(--title-red) 30%, var(--title-rose) 55%, var(--title-red) 75%, var(--title-plum) 100%);
    -webkit-background-clip: text;
    background-clip: text;
    color: transparent;
  }

  .title-line {
    display: block;
    white-space: nowrap;
  }

  .title-line--first {
    padding-left: 96px;
    font-size: 100px;
    letter-spacing: 0.01em;
  }

  .title-small {
    font-size: 68px;
    margin-right: 22px;
  }

  .title-line--second {
    padding-left: 74px;
    margin-top: 6px;
    font-size: 110px;
    letter-spacing: 0.01em;
  }

  .title-initial {
    font-size: 152px;
  }

  .cover-author {
    position: absolute;
    left: 0;
    top: 1088px;
    width: 800px;
    text-align: center;
    font-family: "Oswald", sans-serif;
    font-weight: 500;
    font-size: 36px;
    letter-spacing: 0.14em;
    color: var(--author-white);
  }
</style>
</head>
<body>
  <main class="cover">
    <div class="cover-scene" role="img" aria-label="Woman with backpack standing at the sea shore, arms raised in victory under a pink sunset sky, above bright blue water and white clouds"></div>

    <h1 class="cover-title">
      <span class="title-line title-line--first"><span class="title-small">HER</span>QUIET</span>
      <span class="title-line title-line--second"><span class="title-initial">C</span>OMPASS</span>
    </h1>

    <p class="cover-author">MAREN HOLT</p>
  </main>
</body>
</html>
```